Web Site

Target Market(s)

CEOs and International Sales & Marketing Directors of International Companies who wish to expand their business reach to Dubai and the Middle East and are looking for a local professional partner to work with.

Requirements
Must have
• Creativity is key. We don't want the normal standard boxes of text and boxes of pics. Be as creative as you like.
Nice to have
• (This is only a suggestion, we welcome your creativity)
- The center of all pages could be large rotating pictures which display professional corporate men/women working in an office, images of Dubai, the UAE, skyscrapers of business towers in Dubai, ..etc.
- Images should reflect Dubai and the Arab World as a modern, fast-paced, growing modern market - Not Traditional)
Should not have
• Not so colorful, the fewer colors you use, the better.
Not Crammed or Busy
Not Traditional but modern

```html
<!DOCTYPE html>
<html lang="en">
<head>
<meta charset="utf-8">
<title>Kestrel Group</title>
<link href="https://fonts.googleapis.com/css2?family=Open+Sans:wght@400;600;700&family=Arimo:ital,wght@0,400;0,700;1,400&display=swap" rel="stylesheet">
<style>
:root{
  --red:#8b2a1a;
  --red-dark:#6e1f12;
  --ink:#222;
  --text:#333;
  --muted:#8a8a8a;
  --line:#dcdcdc;
  --bg:#fff;
}
*{margin:0;padding:0;box-sizing:border-box}
html,body{width:1200px;height:933px;overflow:hidden;background:var(--bg)}
body{position:relative;font-family:Arimo,Arial,sans-serif;color:var(--text);
  background:linear-gradient(#f3f5f7 0,#fff 90px)}
.abs{position:absolute}
.brand{left:120px;top:30px;font-family:"Open Sans",sans-serif;font-weight:700;font-size:26px;color:var(--ink);letter-spacing:1px;line-height:1;display:flex;align-items:center;gap:8px}
.brand .mark{width:14px;height:14px;background:var(--ink)}
.util{right:120px;top:21px;font-size:11px;color:var(--muted)}
.util a{color:var(--muted);text-decoration:none}
.util a.hot{color:var(--red)}
.util span{margin:0 5px;color:#bbb}
.search{left:877px;top:55px;width:203px;height:25px;display:flex}
.search input{flex:1;border:1px solid #d5d5d5;border-right:0;border-radius:3px 0 0 3px;font:italic 11px Arimo,sans-serif;padding:0 8px;color:#aaa}
.search button{width:36px;border:0;background:var(--red);border-radius:0 3px 3px 0;display:flex;align-items:center;justify-content:center}
.nav{left:120px;top:101px;width:960px;height:36px;background:linear-gradient(#f7f7f7,#e4e4e4);border-bottom:4px solid var(--red);display:flex;font-family:"Open Sans",sans-serif;font-size:13px}
.nav a{color:#444;text-decoration:none;height:32px;line-height:32px;text-align:center}
.nav a.on{background:var(--red);color:#fff;border-radius:3px 3px 0 0}
.hero{left:120px;top:138px;width:960px;height:321px;border-radius:0 0 4px 4px;overflow:hidden;
  background:linear-gradient(180deg,#8aa0b8 0%,#b7b7ba 30%,#8a8076 60%,#4b4743 100%)}
.hero .person{position:absolute;right:0;bottom:0;width:410px;height:290px;background:linear-gradient(90deg,rgba(240,240,240,0) 0,#e6e3df 35%,#f4f2ef 100%)}
.caption{position:absolute;left:0;top:111px;width:457px;height:210px;background:rgba(40,40,45,.55);padding:27px 0 0 27px;color:#fff}
.caption h1{font-family:"Open Sans",sans-serif;font-weight:400;font-size:22px;line-height:1;margin-bottom:6px}
.caption p{font-size:13px;line-height:15.5px;color:#e6e6e6;width:430px}
.more{display:inline-flex;align-items:center;gap:14px;margin-top:21px;background:var(--red);color:#fff;font-size:11px;height:22px;padding:0 8px}
.dots{display:flex;gap:14px;margin-top:38px}
.dots i{width:9px;height:9px;border-radius:50%;background:#bbb}
.dots i:first-child{background:#fff}
.chair{left:120px;top:481px;width:960px;display:flex;align-items:center;font-size:12px}
.chair h2{font-family:"Open Sans",sans-serif;font-weight:400;font-size:17px;color:var(--ink);letter-spacing:-.3px}
.chair em{color:var(--red)}
.rule{left:120px;width:960px;height:1px;background:var(--line)}
.shade{left:120px;top:500px;width:960px;height:22px;background:linear-gradient(rgba(0,0,0,0),rgba(0,0,0,.04))}
.side{left:122px;top:540px;width:291px}
.side h2{font-family:"Open Sans",sans-serif;font-weight:400;font-size:17px;color:var(--ink);letter-spacing:-.3px;padding-bottom:10px;border-bottom:2px solid #ddd;margin-left:-2px}
.side h3{font-family:"Open Sans",sans-serif;font-weight:400;font-size:13px;color:var(--red);margin-top:11px}
.side p{font-size:12px;line-height:14.5px;margin-top:4px;width:290px}
.panel{left:473px;top:545px;width:607px;height:196px;border:1px solid var(--line);border-radius:4px;background:linear-gradient(#fff 60%,#f4f4f4);padding:17px 18px 0 18px;box-shadow:-18px 0 18px -18px rgba(0,0,0,.12)}
.panel h2{font-family:"Open Sans",sans-serif;font-weight:400;font-size:13px;color:var(--ink);display:flex;align-items:center;gap:10px}
.panel h2 b{font-weight:400;color:var(--red);font-size:14px}
.panel .sub{font-size:10px;margin-top:2px}
.rss{position:absolute;right:18px;top:19px}
.tabs{display:flex;align-items:center;font-size:12px;color:#999;margin-top:23px}
.tabs .sep{margin:0 8px;color:#bbb}
.tabs .on{background:var(--red);color:#fff;border-radius:3px;padding:1px 4px}
.panel p.body{font-size:12px;line-height:14.5px;margin-top:12px;padding-left:2px;width:570px}
.social{left:0;top:808px;width:1200px;display:flex;justify-content:center;gap:22px;font-family:"Open Sans",sans-serif;font-weight:700;font-size:15px;color:#9a9a9a}
.foot{left:0;width:1200px;text-align:center;font-size:11px;color:var(--ink)}
.foot a{color:var(--red);text-decoration:none}
</style>
</head>
<body>
<div class="abs brand"><span class="mark"></span>KESTREL GROUP</div>

<div class="abs util"><a href="#">Login</a><span>|</span><a class="hot" href="#">Carrers</a><span>|</span><a href="#">Sitemap</a><span>|</span><a href="#">Help</a></div>

<form class="abs search"><input value="Search keyword..." aria-label="Search"><button type="button" aria-label="Search">
<svg width="14" height="14" viewBox="0 0 14 14"><circle cx="6" cy="6" r="4.2" fill="none" stroke="#fff" stroke-width="2"/><line x1="9" y1="9" x2="12.5" y2="12.5" stroke="#fff" stroke-width="2.2" stroke-linecap="round"/></svg></button></form>

<nav class="abs nav">
  <a class="on" href="#" style="width:63px">Home</a>
  <a href="#" style="width:168px">About the Group</a>
  <a href="#" style="width:131px">Chairman’s Message</a>
  <a href="#" style="width:132px">Divisions</a>
  <a href="#" style="width:148px">Group Companies</a>
  <a href="#" style="width:214px">Employment &amp; Association</a>
  <a href="#" style="width:104px">Contact us</a>
</nav>

<section class="abs hero" role="img" aria-label="Dubai business district skyline with a professional in traditional attire">
  <div class="person"></div>
  <div class="caption">
    <h1>Kestrel Business Services</h1>
    <p>Kestrel Business Services is an experienced company with a regional focus while maintaining a global representation. Our spectrum of services covers all aspects of doing business in the UAE.</p>
    <span class="more">Readmore <svg width="5" height="7"><path d="M0 0L5 3.5L0 7Z" fill="#d98a7a"/></svg></span>
    <div class="dots"><i></i><i></i><i></i><i></i></div>
  </div>
</section>

<div class="abs shade"></div>
<div class="abs chair">
  <h2>Chairman’s Message</h2>
  <svg width="6" height="8" style="margin:0 14px 0 14px"><path d="M0 0L6 4L0 8Z" fill="var(--red)"/></svg>
  <span>Kestrel Group was founded at the time the United Arab Emirates became an independent nation. From modest beginnings, the <em>Readmore...</em></span>
</div>
<div class="abs rule" style="top:522px"></div>

<aside class="abs side">
  <h2>Employment &amp; Alliances</h2>
  <h3>Employment</h3>
  <p>For Employment opportunities with us, please contact us on info@kestrelgroup.com and attach your CV with a recent photograph and the position you are interested in.</p>
  <h3>Alliances</h3>
  <p>For Strategic Association opportunities with us, please contact us on info@kestrelgroup.com.</p>
</aside>

<section class="abs panel">
  <h2>Group Companies <svg width="6" height="8"><path d="M0 0L6 4L0 8Z" fill="var(--red)"/></svg> <b>Legal Consultation</b></h2>
  <div class="sub">The Firm services include the following</div>
  <svg class="rss" width="16" height="16" viewBox="0 0 16 16"><rect width="16" height="16" rx="2" fill="#f08a24"/><circle cx="4.5" cy="11.5" r="1.6" fill="#fff"/><path d="M3 7a6 6 0 0 1 6 6M3 3.5a9.5 9.5 0 0 1 9.5 9.5" fill="none" stroke="#fff" stroke-width="1.8"/></svg>
  <div class="tabs"><span class="on">Litigation</span><span class="sep">|</span>Dispute Resolutions<span class="sep">|</span>Legal Consultations<span class="sep">|</span>Registration &amp; Incorporation<span class="sep">|</span>Free Zones</div>
  <p class="body">This includes representing Clients and appearing before all courts of different types and levels being a Court of First Instance, Appeal, Cassation, Execution, Examination or Interrogation, Notary Public, Public Prosecutor and other judicial bodies, Police Department, and all other official local/foreign Authorities, Departments, national references and Ministries within UAE or abroad ..attend investigations, to serve notice(s), to file, defend, follow up and execute claims … etc.</p>
</section>

<div class="abs rule" style="top:775px"></div>
<div class="abs social"><span>chirper</span><span>viewtube</span><span>friendbook</span></div>
<div class="abs foot" style="top:847px">+971 4 218 6640 &nbsp;|&nbsp; <a href="#">info@kestrelgroup.com</a></div>
<div class="abs foot" style="top:864px">© 2012 KESTREL Group. All rights reserved. Legal Privacy</div>
</body>
</html>
```